Re design and optimization of a website for pension Ora Vahi, a b&b in Tahiti, French Polynesia.

We have a website already : www.pensionoravahi.example

The general idea is to create a new site that is colorful, young and with an exotic, tropical feel since we are on a beautiful island.

The website will be in three languages, all the text is already available on our website, nothing changes.

All pages must have the name of the website (pension ora vahi b&b) our address, mail and phone number
It would be nice to have a link to our mail from every page

Sections have to be easy to update : text and pics

The sections needed are :

- Home page (accueil)

- Prices (tarifs)

- Bookings (reservations) = link to our mailbox : pensionoravahi@post.example )

- Pictures : in three separate categories that will pop up on this page : 1/ pics of the b&b 2/ pics of the surroundings 3/ customer's pics (we'll give new pics, not the current ones)

- Map of Tahiti : we'd like one map that we'll give you and also a Google map with our location, date and local time would be great

- Links (liens)

We let you see what would look best for the top banner and the switches, matching the logo and the pictures, make it nice and tropical !!
We have a few layouts that we did, maybe you will have a better idea of what we want by looking at them, if you can use them and have a good overall feel

We'd like to remind you guys that Tahiti is a dream destination, so you have to come up with something that the visitors will go : wow !!

We cater for backpackers to mid range accommodations and families, it all about a relaxed friendly atmosphere here !

NOTE THAT WE DON'T KNOW MUCH ABOUT PROGRAMMING AND CODING SO IT AS TO BE READY TO GO ON-LINE, ALL YOUR HELP IS APPRECIATED !!!
Also in Tahiti, the
INTERNET is quite low bandwidth so optimization is a must !

P.S : Live demo of the homepage is welcome ;)

We are available to all you for extra infos, good luck

regards,

remy & Pension Ora Vahi

Target Market(s)

Families and couples : individual rooms

Backpackers : Dormitories

people looking for an authentic stay in a familial environment

Customers of all ages and all nationalities

Requirements
Must have
• You must insist on the main page about :
the easy beach access
the breakfast included (with French baguette !)
Airport pick up 24/7
Many activities departing from our place : scuba diving, canyoning, 4x4 tour, rental cars, surf school, para-glide....

Please find a great way to highlight these !

```html
<!DOCTYPE html>
<html lang="en">
<head>
<meta charset="utf-8">
<title>Pension Ora Vahi</title>
<link href="https://fonts.googleapis.com/css2?family=Fenix&family=Cabin:ital,wght@0,400;0,600;1,400&display=swap" rel="stylesheet">
<style>
:root{
  --orange-deep:#f2571b;
  --orange:#f7931e;
  --yellow:#fbbf1a;
  --yellow-light:#ffd21f;
  --green:#2a7a1e;
  --green-dark:#1d5e14;
  --green-text:#2e6b12;
  --accent:#e8541a;
  --white:#ffffff;
  --rule:#bdbdbd;
}
*{box-sizing:border-box;margin:0;padding:0}
html,body{width:930px;height:1200px;overflow:hidden}
body{position:relative;font-family:"Cabin",sans-serif;color:var(--green-text);
  background:linear-gradient(180deg,var(--orange-deep) 0%,#f4741e 30%,var(--orange) 70%,#f9a51e 100%)}
.abs{position:absolute}
.leaf-fringe{left:0;top:0;width:930px;height:14px;background:linear-gradient(180deg,#2f7d1e,#4a9a2a)}
.decor{background:radial-gradient(circle,#ffb347 0%,rgba(255,120,40,0) 70%)}
.brand{left:73px;top:40px;font-family:"Fenix",serif;font-size:40px;color:var(--yellow-light);letter-spacing:1px}
.nav-band{left:10px;top:115px;width:910px;height:55px;background:linear-gradient(180deg,#3f922a,var(--green) 60%,var(--green-dark));border-radius:3px;box-shadow:0 3px 4px rgba(0,0,0,.25)}
.nav-band::before{content:"";position:absolute;left:53px;right:53px;top:-7px;height:7px;background:var(--yellow);border-radius:4px 4px 0 0}
.nav{left:96px;top:125px;display:flex;gap:0;list-style:none;font-family:"Fenix",serif;font-size:15px;color:var(--yellow-light)}
.nav li{padding:4px 0;height:28px;line-height:20px}
.nav li.active{background:var(--green-dark);border-radius:14px;padding:4px 18px;color:#fff}
.social{top:126px;width:27px;height:27px;border-radius:50%;background:#2f7a1e;box-shadow:inset 0 0 0 2px #246315}
.hero{left:63px;top:162px;width:803px;height:310px;background:linear-gradient(180deg,var(--yellow-light),var(--yellow))}
.hero h1{left:46px;top:52px;width:360px;font-family:"Fenix",serif;font-weight:400;font-size:30px;line-height:32px;color:var(--green-dark)}
.hero p{left:46px;top:122px;width:320px;font-family:"Fenix",serif;font-size:12.3px;line-height:16px;color:var(--green-dark)}
.btn{top:198px;height:26px;line-height:26px;font-family:"Fenix",serif;font-size:11px;color:#fff;text-align:center;border-radius:2px}
.btn-book{left:45px;width:89px;background:var(--green)}
.btn-more{left:141px;width:81px;background:#f75b1c}
.frame{border-radius:50%;border:6px dotted #fff;background:radial-gradient(circle,#4f8d33,#2d6a1d)}
.frame.beach{background:linear-gradient(180deg,#6fb0d6 0%,#9fcde4 45%,#e6d7a8 60%,#cdb47f 100%)}
.dots{left:379px;top:265px;display:flex;gap:4px}
.dots span{width:9px;height:9px;border-radius:50%;background:#fff}
.dots span:first-child{background:#6b4a12}
.sun{right:0;top:0;width:130px;height:110px;background:radial-gradient(circle at 80% 20%,#ffe14a,#f5b800 60%,rgba(251,191,26,0) 80%)}
.panel{left:63px;top:468px;width:803px;height:682px;background:var(--white);border-radius:0 0 6px 6px}
.wave{left:63px;top:452px}
h2{font-family:"Fenix",serif;font-weight:400;font-size:17px;color:var(--green-dark)}
h2 .hi{color:var(--accent)}
h2.orange{color:var(--accent)}
.photo{border:3px solid #fff;box-shadow:0 0 0 1px #d6d6d6,0 1px 4px rgba(0,0,0,.2)}
.lead{font-family:"Fenix",serif;font-size:13px;color:var(--green-dark)}
.body-text{font-size:10px;line-height:16px}
.body-text p+p{margin-top:4px}
.rule{left:85px;width:761px;border-top:1px dotted var(--rule)}
.why p{font-size:9.5px;line-height:16.2px;text-align:justify}
.why p.strong{font-weight:600}
.why p+p{margin-top:4px}
.readmore{font-size:10px;font-weight:600;color:var(--green-dark)}
.testi{left:476px;width:370px}
.testi .face{width:70px;height:55px;border-radius:2px;background:linear-gradient(135deg,#c9a07d,#6b4a35)}
.testi h3{font-size:10px;font-weight:600;line-height:16px}
.testi p{font-size:10px;font-style:italic;line-height:16px}
.gallery .photo{top:995px;width:176px;height:104px}
.footer{left:0;width:930px;top:1165px;text-align:center;font-size:10px;color:var(--green-dark);font-weight:600}
</style>
</head>
<body>
<div class="abs leaf-fringe" role="img" aria-label="Row of green tropical leaves"></div>
<div class="abs decor" style="left:640px;top:10px;width:290px;height:110px" role="img" aria-label="Tropical flower decoration"></div>
<div class="abs decor" style="left:-40px;top:180px;width:110px;height:600px" role="img" aria-label="Tropical flower decoration"></div>

<div class="abs brand">Pension Ora Vahi</div>

<div class="abs nav-band"></div>
<ul class="abs nav">
  <li class="active">Main</li>
  <li style="margin-left:42px">Pricing</li>
  <li style="margin-left:55px">Booking</li>
  <li style="margin-left:55px">Photos</li>
  <li style="margin-left:55px">Locations</li>
  <li style="margin-left:55px">Contact</li>
</ul>
<div class="abs social" style="left:777px"></div>
<div class="abs social" style="left:813px"></div>

<section class="abs hero">
  <div class="abs sun" role="img" aria-label="Sunflowers"></div>
  <h1 class="abs">Pension Ora Vahi Puch Line goes here</h1>
  <p class="abs">Lorem ipsum dolor sit amet, consectetuer adipiscing elit. Nam cursus. Morbi ut mi. Nullam enim leo, egestas id, condimentum at, laoreet mattis, massa. Sed eleifend nonummy diam.</p>
  <div class="abs btn btn-book">Booking Now</div>
  <div class="abs btn btn-more">Learn More</div>
  <div class="abs frame" style="left:420px;top:10px;width:200px;height:165px" role="img" aria-label="Garden of the pension, family atmosphere"></div>
  <div class="abs frame beach" style="left:545px;top:110px;width:220px;height:165px" role="img" aria-label="Beach access 200 metres from the pension"></div>
  <div class="abs dots"><span></span><span></span><span></span><span></span></div>
</section>

<svg class="abs wave" width="803" height="24" viewBox="0 0 803 24" aria-hidden="true">
  <path d="M0 16 C200 8 400 24 600 14 S780 4 803 2 L803 24 L0 24 Z" fill="#fff"/>
</svg>
<main class="abs panel"></main>

<h2 class="abs" style="left:88px;top:478px"><span class="hi">Welcome</span> to Our Website Mainpage</h2>
<div class="abs photo" style="left:88px;top:507px;width:208px;height:138px;background:linear-gradient(135deg,#9a6a3a,#5a3b22 60%,#8fa46a)" role="img" aria-label="Guests sharing a meal on the terrace"></div>
<div class="abs" style="left:311px;top:508px;width:535px">
  <div class="lead">Lorem ipsum dolor sit amet, consectetuer adipiscing elit.</div>
  <div class="body-text" style="margin-top:5px">
    <p>Nam cursus. Morbi ut mi. Nullam enim leo, egestas id, condimentum at, laoreet mattis, massa. Sed eleifend nonummy diam. Praesent mauris ante, elementum et, bibendum at, posuere sit amet, nibh.</p>
    <p>Morbi ornare gravida elit. Integer congue, augue et malesuada iaculis, ipsum dui aliquet felis, at cursus magna nisl nec elit. Donec iaculis diam a nisi accumsan viverra. Duis sed tellus et tortor vestibulum gravida. Praesent elementum elit at tellus. Curabitur metus ipsum, luctus eu, malesuada ut, tincidunt sed, diam. Donec quis mi sed magna hendrerit accumsan. Suspendisse risus nibh, ultricies eu, volutpat non, condimentum hendrerit, augue. Etiam eleifend, metus vitae adipiscing semper, mauris ipsum iaculis elit, congue gravida elit mi egestas orci. Curabitur pede.</p>
  </div>
</div>

<div class="abs rule" style="top:675px"></div>

<h2 class="abs orange" style="left:85px;top:697px">Why We Are</h2>
<div class="abs photo" style="left:85px;top:727px;width:106px;height:163px;background:linear-gradient(180deg,#7fb2d9,#8a6a4a 50%,#c4322a 80%,#5a7a3a)" role="img" aria-label="Islander carrying a stone at a traditional festival"></div>
<div class="abs why" style="left:204px;top:724px;width:241px">
  <p class="strong">Nunc tempus felis vitae urna. Vivamus porttitor, neque at volutpat rutrum, purus nisi eleifend libero, a tempus libero lectus feugiat felis. Morbi diam mauris, viverra in, gravida eu, mattis in, ante.</p>
  <p>Morbi eget arcu. Morbi porta, libero id ullamcorper nonummy, nibh ligula pulvinar metus, eget consectetuer augue nisi quis lacus. Ut ac mi quis lacus mollis aliquam.</p>
  <p>Curabitur iaculis tempus eros. Curabitur vel mi sit amet magna malesuada ultrices. Ut nisi erat, fermentum vel, congue id, euismod in, elit.</p>
</div>
<div class="abs readmore" style="left:204px;top:900px">READ MORE <svg width="6" height="8" viewBox="0 0 6 8"><path d="M0 0 L6 4 L0 8 Z" fill="currentColor"/></svg></div>

<h2 class="abs orange" style="left:473px;top:697px">Customer Testimonials</h2>
<div class="abs testi" style="top:723px">
  <div class="abs face" style="left:0;top:0" role="img" aria-label="Portrait of a guest"></div>
  <div class="abs" style="left:81px;top:0;width:280px"><h3>Nam cursus. Morbi ut mi.</h3><p>Nullam enim leo, egestas id, condimentum at, laoreet mattis, massa. Sed eleifend nonummy diam.</p></div>
  <div class="abs face" style="left:0;top:67px" role="img" aria-label="Portrait of a guest"></div>
  <div class="abs" style="left:81px;top:67px;width:280px"><h3>Ut velit enim, vestibulum non, fermentum nec</h3><p>Nullam enim leo, egestas id, condimentum at, laoreet mattis, massa. Sed eleifend nonummy diam.</p></div>
  <div class="abs face" style="left:0;top:142px" role="img" aria-label="Portrait of a guest"></div>
  <div class="abs" style="left:82px;top:140px;width:280px"><h3>Curabitur iaculis tempus eros. Curabitur vel mi sit amet magna malesuada ultrices.</h3><p>Nullam enim leo, egestas id, condimentum at, laoreet mattis, massa. Sed eleifend nonummy diam.</p></div>
</div>

<div class="abs rule" style="top:948px"></div>

<h2 class="abs orange" style="left:88px;top:965px">Gallery &amp; Photos</h2>
<div class="gallery">
  <div class="abs photo" style="left:88px;background:linear-gradient(180deg,#4f8fd0,#9cc7e4 45%,#d8cfae 70%,#b8a47a)" role="img" aria-label="Lagoon beach"></div>
  <div class="abs photo" style="left:278px;background:linear-gradient(180deg,#8a6b4a,#b8936a 35%,#f1ead8 55%,#3f7a2a)" role="img" aria-label="Thatched bungalows"></div>
  <div class="abs photo" style="left:469px;background:linear-gradient(180deg,#6e9a4a,#3f7a2a 50%,#7fae4a)" role="img" aria-label="Palm garden lawn"></div>
  <div class="abs photo" style="left:660px;background:linear-gradient(180deg,#5a8a3a,#2d5f1d 50%,#6ea83a)" role="img" aria-label="Tropical garden"></div>
</div>

<div class="abs footer">© 2012 Company Name &nbsp;|&nbsp; All right reserved &nbsp;|&nbsp; Term &amp; Conditions</div>
</body>
</html>
```